Business Card Design Project

We require a business card template to cover basic contact information - our company logo, names of employees, title, mobile and email.

Target Market(s)

Corporate

Industry/Entity Type

Business

Font styles to use
Sans Serif

Requirements
Nice to have
• Thinking it would be great just to have the logo taking up approximately half the space (so it goes as far across the top of the card as possible) and then contact details in the lower half of the card. Keen just to use only the two colours in the logo, on a white background.
Should not have
• No fussy drawings

```html
<!DOCTYPE html>
<html lang="en">
<head>
<meta charset="utf-8">
<title>Larkfield Developments – Business Card</title>
<link rel="stylesheet" href="https://fonts.googleapis.com/css2?family=Arimo:wght@400;600&display=swap">
<style>
  :root {
    --backdrop: #d6d6d6;
    --card: #ffffff;
    --teal: #2ba3b1;
    --blue: #2b55a6;
    --shadow: rgba(0, 0, 0, 0.18);
  }
  * { box-sizing: border-box; margin: 0; padding: 0; }
  html, body {
    width: 1200px;
    height: 900px;
    overflow: hidden;
    background: var(--backdrop);
    font-family: "Arimo", Arial, sans-serif;
  }
  .business-card {
    position: absolute;
    left: 100px;
    top: 145px;
    width: 1000px;
    height: 610px;
    background: var(--card);
    border-radius: 44px;
    box-shadow: 0 14px 40px var(--shadow);
    overflow: hidden;
  }
  .brand-name {
    position: absolute;
    left: 0;
    right: 0;
    top: 120px;
    text-align: center;
    color: var(--teal);
    font-weight: 600;
    font-size: 92px;
    letter-spacing: -1px;
    line-height: 1;
  }
  .brand-band {
    position: absolute;
    left: 0;
    right: 0;
    top: 318px;
    height: 16px;
    background: var(--teal);
  }
  .person {
    position: absolute;
    left: 40px;
    width: 290px;
    top: 400px;
    text-align: right;
  }
  .person-name {
    color: var(--blue);
    font-size: 36px;
    font-weight: 400;
    line-height: 1.2;
  }
  .person-title {
    color: var(--teal);
    font-size: 32px;
    line-height: 1.3;
  }
  .divider {
    position: absolute;
    left: 358px;
    top: 385px;
    width: 2px;
    height: 135px;
    background: var(--teal);
  }
  .contact-list {
    position: absolute;
    left: 392px;
    top: 396px;
    list-style: none;
  }
  .contact-item {
    display: flex;
    align-items: center;
    gap: 10px;
    color: var(--blue);
    font-size: 32px;
    line-height: 1;
    height: 48px;
  }
  .contact-icon {
    width: 36px;
    height: 36px;
    flex: none;
  }
</style>
</head>
<body>
  <main class="business-card">
    <h1 class="brand-name">Larkfield Developments</h1>
    <div class="brand-band"></div>

    <div class="person">
      <p class="person-name">Milo Hart</p>
      <p class="person-title">Manager</p>
    </div>

    <div class="divider"></div>

    <ul class="contact-list">
      <li class="contact-item">
        <svg class="contact-icon" viewBox="0 0 24 24" aria-hidden="true">
          <path fill="#2ba3b1" d="M6.6 10.8c1.4 2.8 3.8 5.1 6.6 6.6l2.2-2.2c.3-.3.7-.4 1-.2 1.1.4 2.3.6 3.6.6.6 0 1 .4 1 1V20c0 .6-.4 1-1 1C10.6 21 3 13.4 3 4c0-.6.4-1 1-1h3.5c.6 0 1 .4 1 1 0 1.3.2 2.5.6 3.6.1.3 0 .7-.2 1l-2.3 2.2z"/>
        </svg>
        <span>0400 517 382</span>
      </li>
      <li class="contact-item">
        <svg class="contact-icon" viewBox="0 0 24 24" aria-hidden="true">
          <rect x="2" y="5" width="20" height="14" rx="1.5" fill="#2ba3b1"/>
          <path d="M2.8 6l9.2 7 9.2-7" fill="none" stroke="#ffffff" stroke-width="1.6"/>
        </svg>
        <span>milohart@example.com</span>
      </li>
    </ul>
  </main>
</body>
</html>
```